Colwyn Marsh Optometry 10 Year Celebration

Front of invitation
Size 107-139mm
Font – Georgia
The invitation should be worded as follows;
Colwyn Marsh Optometry
would like to invite you to...

```html
<!DOCTYPE html>
<html lang="en">
<head>
<meta charset="utf-8">
<title>Colwyn Marsh Optometry – 10 Year Celebration Invitation</title>
<link href="https://fonts.googleapis.com/css2?family=Gelasio:ital,wght@0,400;0,700;1,400&display=swap" rel="stylesheet">
<style>
  :root {
    --canvas: #f2f2f2;
    --ink-black: #151314;
    --paper-white: #ffffff;
    --copper-light: #e2a888;
    --copper-deep: #b5724c;
    --copper-text: #2e1f18;
    --copper-stripe: #f7f5f3;
    --violet-light: #6a5590;
    --violet-deep: #3b2c4b;
    --violet-text: #241b2e;
    --violet-stripe: #ebe2f1;
    --serif: Georgia, "Gelasio", serif;
  }
  * { box-sizing: border-box; margin: 0; padding: 0; }
  html, body { width: 1200px; height: 1200px; overflow: hidden; background: var(--canvas); }
  body { position: relative; font-family: var(--serif); }

  .card {
    position: absolute; width: 544px; height: 419px;
    background: var(--ink-black); overflow: hidden;
    box-shadow: 0 2px 6px rgba(0,0,0,0.22);
  }
  .card--front-copper { left: 36px; top: 158px; }
  .card--back-copper  { left: 620px; top: 158px; }
  .card--front-violet { left: 36px; top: 636px; }
  .card--back-violet  { left: 620px; top: 636px; }

  .card--copper { --accent-light: var(--copper-light); --accent-deep: var(--copper-deep); --accent-text: var(--copper-text); --stripe: var(--copper-stripe); }
  .card--violet { --accent-light: var(--violet-light); --accent-deep: var(--violet-deep); --accent-text: var(--violet-text); --stripe: var(--violet-stripe); }

  /* Front */
  .stripe { position: absolute; left: 0; width: 100%; background: var(--stripe); }
  .stripe--upper { top: 76px; height: 82px; }
  .stripe--lower { top: 255px; height: 86px; }

  .confetti-halo {
    position: absolute; left: 52px; top: 2px; width: 440px; height: 414px; border-radius: 50%;
    background: radial-gradient(closest-side, var(--accent-deep) 62%, color-mix(in srgb, var(--accent-deep) 55%, transparent) 80%, transparent 100%);
  }
  .medallion {
    position: absolute; left: 117px; top: 57px; width: 310px; height: 310px; border-radius: 50%;
    background: radial-gradient(circle at 65% 70%, var(--accent-light) 0%, var(--accent-deep) 95%);
  }

  .front-text { position: absolute; left: 0; width: 544px; text-align: center; white-space: nowrap; }
  .brand-name { top: 74px; font-size: 20px; color: var(--paper-white); }
  .invite-line { top: 117px; font-size: 15px; color: var(--accent-text); }
  .celebrate-lettering {
    position: absolute; left: 108px; top: 138px; width: 344px; height: 90px; border-radius: 40px;
    background: linear-gradient(180deg, rgba(255,255,255,0.92), rgba(255,255,255,0.78));
  }
  .anniversary { top: 224px; font-size: 19px; color: var(--paper-white); }
  .location-heading { top: 252px; font-size: 20px; font-weight: 700; letter-spacing: 0.3px; color: var(--accent-text); }
  .address { top: 279px; font-size: 15px; letter-spacing: -0.3px; color: var(--paper-white); }
  .event-date { top: 301px; font-size: 15px; font-style: italic; color: var(--accent-text); }
  .event-time { top: 323px; font-size: 17px; letter-spacing: -0.3px; color: var(--accent-text); }

  /* Back */
  .confetti-fall {
    position: absolute; left: 0; top: 0; width: 100%; height: 180px;
    background: linear-gradient(180deg, var(--accent-light) 0%, color-mix(in srgb, var(--accent-deep) 70%, transparent) 35%, color-mix(in srgb, var(--accent-deep) 25%, transparent) 70%, transparent 100%);
  }
  .back-heading {
    position: absolute; left: 0; top: 100px; width: 100%; text-align: center;
    font-size: 21px; font-weight: 700; line-height: 19px; color: var(--paper-white);
  }
  .back-body {
    position: absolute; left: 0; top: 166px; width: 100%; text-align: center;
    font-size: 13.5px; line-height: 19.5px; color: var(--paper-white);
  }
  .back-body p + p { margin-top: 19.5px; }
</style>
</head>
<body>

  <section class="card card--front-copper card--copper" aria-label="Invitation front, copper">
    <div class="stripe stripe--upper"></div>
    <div class="stripe stripe--lower"></div>
    <div class="confetti-halo" role="img" aria-label="Ring of scattered copper confetti dots"></div>
    <div class="medallion"></div>
    <p class="front-text brand-name">Colwyn Marsh Optometry</p>
    <p class="front-text invite-line">would like to invite you to...</p>
    <div class="celebrate-lettering" role="img" aria-label="Hand lettered word Celebrate in white"></div>
    <p class="front-text anniversary">Our 10 Year Anniversary!</p>
    <p class="front-text location-heading">IN OUR NEW LOCATION</p>
    <p class="front-text address">42 Harbour Lane  Tallowbrook NSW</p>
    <p class="front-text event-date">Tuesday 12th December</p>
    <p class="front-text event-time">11.00 am - 7.00 pm</p>
  </section>

  <section class="card card--back-copper card--copper" aria-label="Invitation back, copper">
    <div class="confetti-fall" role="img" aria-label="Copper confetti dots falling from the top edge"></div>
    <h2 class="back-heading">You are personally invited to come and<br>experience our brand new store!</h2>
    <div class="back-body">
      <p>Be one of the first to come in as well as a chance to try<br>on some of our new frames.<br>There will be special guests including a colour<br>consultant and brand representatives,<br>Refreshments and nibbles provided.<br>Champagne into the evening.</p>
      <p>We would love the opportunity to celebrate with our<br>local community so bring along your friends and family</p>
    </div>
  </section>

  <section class="card card--front-violet card--violet" aria-label="Invitation front, violet">
    <div class="stripe stripe--upper"></div>
    <div class="stripe stripe--lower"></div>
    <div class="confetti-halo" role="img" aria-label="Ring of scattered violet confetti dots"></div>
    <div class="medallion"></div>
    <p class="front-text brand-name">Colwyn Marsh Optometry</p>
    <p class="front-text invite-line">would like to invite you to...</p>
    <div class="celebrate-lettering" role="img" aria-label="Hand lettered word Celebrate in white"></div>
    <p class="front-text anniversary">Our 10 Year Anniversary!</p>
    <p class="front-text location-heading">IN OUR NEW LOCATION</p>
    <p class="front-text address">42 Harbour Lane  Tallowbrook NSW</p>
    <p class="front-text event-date">Tuesday 12th December</p>
    <p class="front-text event-time">11.00 am - 7.00 pm</p>
  </section>

  <section class="card card--back-violet card--violet" aria-label="Invitation back, violet">
    <div class="confetti-fall" role="img" aria-label="Violet confetti dots falling from the top edge"></div>
    <h2 class="back-heading">You are personally invited to come and<br>experience our brand new store!</h2>
    <div class="back-body">
      <p>Be one of the first to come in as well as a chance to try<br>on some of our new frames.<br>There will be special guests including a colour<br>consultant and brand representatives,<br>Refreshments and nibbles provided.<br>Champagne into the evening.</p>
      <p>We would love the opportunity to celebrate with our<br>local community so bring along your friends and family</p>
    </div>
  </section>

</body>
</html>
```